21 ERP project mistakes to avoid

I am looking for a document template for a white paper of about 20 pages that discusses 21 mistakes you can make when selecting or implementing erp software. The audience is corporate - typically managers charged with leading an erp selection or implementation project. I want something modern and minimalist. I,m assuming the template would need to be in MS Word but the delivery format would be PDF. This not really a brochure but there is no closer category to this on the site.

Target Market(s)

Corporate enterprise software managers

Font styles to use
Serif
Sans Serif

Colors
0493ce

Requirements
Must have
• Modern,minimalist look. MS Word template or a template I can imoprt text into and convert to PDF for publishing via a web link to the document
Nice to have
• Creative front page and headings for each piece of '21 mistakes' content.plenty of white space in design.
Should not have
• Lots of crammed text and boring headings

```html
<!DOCTYPE html>
<html lang="en">
<head>
<meta charset="utf-8">
<title>21 Mistakes – ERP Project Mistakes to Avoid</title>
<link href="https://fonts.googleapis.com/css2?family=Montserrat:wght@300;400&family=Roboto:wght@300;400&display=swap" rel="stylesheet">
<style>
  :root {
    --brand-blue: #0493ce;
    --brand-deep: #0a6fb8;
    --ink: #2b2b2b;
    --muted: #4a4a4a;
    --paper: #ffffff;
    --backdrop: #e6e7e9;
    --photo-light: #d6d6d6;
    --photo-dark: #555555;
  }
  * { margin: 0; padding: 0; box-sizing: border-box; }
  html, body { width: 1200px; height: 935px; overflow: hidden; }
  body { background: var(--backdrop); position: relative; font-family: "Roboto", Arial, sans-serif; }

  .page {
    position: absolute;
    top: 99px;
    width: 503px;
    height: 711px;
    background: var(--paper);
    overflow: hidden;
    box-shadow: 0 2px 10px rgba(0,0,0,.12);
  }
  .page--cover { left: 62px; }
  .page--inside { left: 603px; }
  .page__art { position: absolute; left: 0; top: 0; width: 503px; height: 711px; }

  .cover-title {
    position: absolute; left: 190px; top: 600px; width: 290px;
    font-family: "Montserrat", sans-serif; color: var(--brand-blue);
  }
  .cover-title__main { font-weight: 400; font-size: 40px; line-height: 1; letter-spacing: -.5px; }
  .cover-title__sub {
    margin-top: 10px; font-weight: 300; font-size: 14px; line-height: 18px;
    text-transform: uppercase; letter-spacing: 1.5px; color: var(--muted);
  }

  .running-foot {
    position: absolute; right: 24px; bottom: 32px; text-align: right;
    font-family: "Montserrat", sans-serif; color: var(--brand-blue);
  }
  .running-foot__main { font-weight: 400; font-size: 18px; line-height: 1; }
  .running-foot__sub {
    margin-top: 4px; font-weight: 300; font-size: 8.5px; letter-spacing: 1px;
    text-transform: uppercase; color: var(--muted);
  }

  .section-heading {
    position: absolute; left: 29px; top: 165px;
    font-family: "Roboto", sans-serif; font-weight: 300;
    font-size: 27px; color: var(--brand-blue); white-space: nowrap;
  }
  .body-column {
    position: absolute; top: 222px;
    font-weight: 300; font-size: 9.7px; line-height: 12.15px; color: var(--ink);
    text-align: justify; hyphens: auto;
  }
  .body-column p + p { margin-top: 12.15px; }
  .body-column--left { left: 21px; width: 229px; }
  .body-column--right { left: 267px; width: 213px; }
</style>
</head>
<body>

<section class="page page--cover">
  <svg class="page__art" viewBox="0 0 503 711" preserveAspectRatio="none">
    <defs>
      <linearGradient id="photoTone" x1="0" y1="0" x2="1" y2="1">
        <stop offset="0" stop-color="var(--photo-light)"/>
        <stop offset="1" stop-color="var(--photo-dark)"/>
      </linearGradient>
    </defs>
    <polygon role="img" aria-label="Black and white photo of a stressed woman at a desk with a laptop, holding her glasses" points="0,0 503,0 503,300 0,420" fill="url(#photoTone)"/>
    <polygon points="0,420 503,300 503,340 0,460" fill="var(--brand-blue)"/>
  </svg>
  <div class="cover-title">
    <div class="cover-title__main">21 Mistakes</div>
    <div class="cover-title__sub">ERP project mistakes<br>to avoid</div>
  </div>
</section>

<section class="page page--inside">
  <svg class="page__art" viewBox="0 0 503 711" preserveAspectRatio="none">
    <rect x="0" y="0" width="503" height="10" fill="var(--brand-blue)"/>
    <rect x="29" y="140" width="40" height="3" fill="var(--brand-blue)"/>
  </svg>

  <h1 class="section-heading">Heading Goes Here</h1>

  <div class="body-column body-column--left">
    <p>"Sed ut perspiciatis unde omnis iste natus error sit voluptatem accusantium doloremque laudantium, totam rem aperiam, eaque ipsa quae ab illo inventore veritatis et quasi architecto beatae vitae dicta sunt explicabo. Nemo enim ipsam voluptatem quia voluptas sit aspernatur aut odit aut fugit, sed quia consequuntur magni dolores eos qui ratione voluptatem sequi nesciunt. Neque porro quisquam est, qui dolorem ipsum quia dolor sit amet, consectetur, adipisci velit, sed quia non numquam eius modi tempora incidunt ut labore et dolore magnam aliquam quaerat voluptatem. Ut enim ad minima veniam, quis nostrum exercitationem ullam corporis suscipit laboriosam, nisi ut aliquid ex ea commodi consequatur? Quis autem vel eum iure reprehenderit qui in ea voluptate velit esse quam nihil molestiae consequatur, vel illum qui dolorem eum fugiat quo voluptas nulla pariatur?"</p>
    <p>"At vero eos et accusamus et iusto odio dignissimos ducimus qui blanditiis praesentium voluptatum deleniti atque corrupti quos dolores et quas molestias excepturi sint occaecati cupiditate non provident, similique sunt in culpa qui officia deserunt mollitia animi, id est laborum et dolorum fuga. Et harum quidem rerum facilis est et expedita distinctio. Nam libero tempore, cum soluta nobis est eligendi optio cumque nihil impedit quo minus id quod maxime placeat facere possimus, omnis voluptas assumenda est, omnis dolor repellendus. Temporibus autem quibusdam et aut officiis debitis aut perferendis doloribus asperiores repellat."</p>
  </div>

  <div class="body-column body-column--right">
    <p>"Sed ut perspiciatis unde omnis iste natus error sit voluptatem accusantium doloremque laudantium, totam rem aperiam, eaque ipsa quae ab illo inventore veritatis et quasi architecto beatae vitae dicta sunt explicabo. Nemo enim ipsam voluptatem quia voluptas sit aspernatur aut odit aut fugit, sed quia consequuntur magni dolores eos qui ratione voluptatem sequi nesciunt. Neque porro quisquam est, qui dolorem ipsum quia dolor sit amet, consectetur, adipisci velit, sed quia non numquam eius modi tempora incidunt ut labore et dolore magnam aliquam quaerat voluptatem. Ut enim ad minima veniam, quis nostrum exercitationem ullam corporis suscipit laboriosam, nisi ut aliquid ex ea commodi consequatur? Quis autem vel eum iure reprehenderit qui in ea voluptate velit esse quam nihil molestiae consequatur, vel illum qui dolorem eum fugiat quo voluptas nulla pariatur?"</p>
  </div>

  <div class="running-foot">
    <div class="running-foot__main">21 Mistakes</div>
    <div class="running-foot__sub">ERP project mistakes to avoid</div>
  </div>
</section>

</body>
</html>
```